New Website for Open Orbit Charity (KELVOR)

We need a dynamic web design for our brand new charity organisation that will be working worldwide. We will be funded by donations so need to attract people to donate.

What We Do
We work to optimise the wellbeing of the planet, the animals and all that live within. Our slogan is Achieving Vibrational Equilibrium.

We have included a Powerpoint document which may help you understand what we need, it is just an idea for structure and style, it is not set in stone so feel free to be as creative as you like!
Updates

Designs look the same

Target Market(s)

Adults 18+ with an interest in animal, environmental. Businesses that may like to support our natural world or already support our natural world.

Number of Pages Required

3 page

Colors

Designer to choose colors to be used in the design.

Requirements
Must have
• We need the website to be easy to use and understand.

Web pages will be Home, What We Do, Who We Are, Success Stories, What You Can Do (Blog section), Seek Help, Donate, Join.
Nice to have
• Natural feel, easy to navigate, Ideally the website will look natural and organic.

Natural colours, blues, greens, sand, gold, brown, grey, silver, Orange and yellow for impact.
Should not have
• Should not have a dark coloured theme.

```html
<!DOCTYPE html>
<html lang="en">
<head>
<meta charset="utf-8">
<title>Open Orbit Charity</title>
<link rel="stylesheet" href="https://fonts.googleapis.com/css2?family=Anton&family=Poppins:wght@400;500;600&display=swap">
<style>
:root{
  --orange:#e0621f;
  --ink:#1d1d1d;
  --text:#6b6b6b;
  --white:#ffffff;
  --footer:#1e1e1e;
  --footer-line:#3a3a3a;
  --footer-text:#8a8a8a;
}
*{margin:0;padding:0;box-sizing:border-box}
html,body{width:1200px;height:3417px;overflow:hidden;background:var(--white)}
body{position:relative;font-family:"Poppins",sans-serif;color:var(--text)}
.abs{position:absolute}
.display{font-family:"Anton",sans-serif;text-transform:uppercase;letter-spacing:-.5px;line-height:1;white-space:nowrap}
.btn{position:absolute;display:flex;align-items:center;justify-content:center;font-weight:600;font-size:11px;letter-spacing:.6px;text-transform:uppercase}
.btn-solid{background:var(--orange);color:var(--white)}
.btn-outline{border:1px solid var(--orange);color:var(--ink);background:var(--white)}
.btn-ghost{border:1px solid var(--white);color:var(--white)}

/* header */
.logo{left:94px;top:48px;font-size:29px;color:var(--ink)}
.nav a{position:absolute;top:58px;font-size:12px;color:var(--ink);text-decoration:none}
.nav a.active{color:var(--orange)}
.header-rule{left:0;top:129px;width:1200px;height:6px;background:var(--orange)}

/* hero */
.hero-photo{left:0;top:135px;width:1200px;height:627px;background:
  radial-gradient(ellipse 420px 320px at 780px 330px,#a3825f 0%,#6f5538 45%,transparent 75%),
  linear-gradient(90deg,#1c2414 0%,#2d3520 35%,#4a4a2c 60%,#5c4a30 100%)}
.hero-kicker{left:94px;top:252px;font-size:35px;color:var(--white)}
.hero-line{position:absolute;left:88px;font-size:116px;line-height:1;color:var(--white)}
.hero-copy{left:94px;top:546px;width:400px;font-size:14px;line-height:25px;color:var(--white)}
.hero-band{left:0;top:678px}
.band-title{left:643px;top:706px;font-size:23px;color:var(--white)}
.band-underline{left:643px;top:738px;width:64px;height:2px;background:var(--white)}

/* cards */
.card-photo{position:absolute;top:908px;width:300px;height:255px;clip-path:polygon(0 0,100% 0,100% 66%,70% 100%,0 100%)}
.card-label{position:absolute;top:1116px;font-size:26px;color:var(--white)}
.card-copy{position:absolute;top:1191px;width:270px;font-size:14px;line-height:25px}
.card-link{position:absolute;top:1268px;font-size:11px;font-weight:600;letter-spacing:.5px;color:var(--orange)}
.divider{left:84px;top:1386px;width:1019px;height:1px;background:#ececec}

/* features */
.feature-photo{position:absolute;width:536px;height:356px;clip-path:polygon(0 0,100% 0,100% 67%,80% 100%,0 100%)}
.feature-title{position:absolute;font-size:44px;color:var(--ink)}
.feature-copy{position:absolute;width:350px;font-size:14px;line-height:25px}
.animal-band{left:0;top:2045px;width:1052px;height:348px;background:var(--orange)}

/* footer */
.footer{left:0;top:3014px;width:1200px;height:352px;background:var(--footer)}
.footer-logo{left:141px;top:3106px;font-size:29px;color:var(--white)}
.footer-copy{left:141px;top:3166px;width:220px;font-size:10px;line-height:17px;color:var(--footer-text)}
.social{position:absolute;top:3240px;width:22px;height:22px;border-radius:50%;background:var(--white)}
.footer-col h4{position:absolute;top:3103px;font-size:16px;font-weight:500;color:var(--white)}
.footer-col a{position:absolute;width:145px;height:31px;padding:7px 0 0 8px;font-size:11px;color:var(--footer-text);text-decoration:none;border-bottom:1px solid var(--footer-line)}
.footer-col a.current{background:#2c2c2c;color:var(--white);font-weight:500}
.copyright{left:0;top:3366px;width:1200px;height:51px;background:var(--orange);display:flex;align-items:center;justify-content:center;font-size:11px;color:var(--white)}
</style>
</head>
<body>

<header>
  <div class="abs display logo">Open Orbit Charity</div>
  <nav class="nav">
    <a class="active" style="left:414px">Home</a>
    <a style="left:473px">What We Do</a>
    <a style="left:569px">Who We Are</a>
    <a style="left:663px">Success Stories</a>
    <a style="left:776px">What You Can Do</a>
  </nav>
  <div class="btn btn-solid" style="left:899px;top:48px;width:107px;height:42px">Donate</div>
  <div class="btn btn-outline" style="left:1020px;top:48px;width:112px;height:42px">Join</div>
  <div class="abs header-rule"></div>
</header>

<section class="hero">
  <div class="abs hero-photo" role="img" aria-label="Young lynx walking across a forest floor"></div>
  <div class="abs display hero-kicker">Help raise world vibration</div>
  <h1>
    <span class="display hero-line" style="top:302px">Healing</span>
    <span class="display hero-line" style="top:418px">The world</span>
  </h1>
  <p class="abs hero-copy">Lorem Ipsum is simply dummy text of the printing and typesetting industry. Lorem Ipsum has been.</p>
  <div class="btn btn-solid" style="left:93px;top:625px;width:164px;height:53px">Make a difference</div>
  <svg class="abs hero-band" width="1200" height="95" viewBox="0 0 1200 95">
    <polygon points="0,84 555,84 617,0 1200,0 1200,84 553,84 545,95 0,95" fill="#e0621f"/>
  </svg>
  <div class="abs display band-title">Help raise world vibration</div>
  <div class="abs band-underline"></div>
</section>

<section class="cards">
  <div class="card-photo" style="left:93px;background:linear-gradient(170deg,#c7702a 0%,#7a4526 45%,#2e2520 100%)" role="img" aria-label="Mountain coastline under an orange sky"></div>
  <div class="card-label display" style="left:116px">Environment</div>
  <p class="card-copy" style="left:94px">Lorem Ipsum is simply dummy text of the printing and typesettin</p>
  <div class="card-link" style="left:94px">FIND OUT MORE &nbsp; &rsaquo;</div>

  <div class="card-photo" style="left:444px;background:linear-gradient(160deg,#8fb0c8 0%,#6e8f64 45%,#4f9a36 100%)" role="img" aria-label="Zebra standing in green grass"></div>
  <div class="card-label display" style="left:469px">Animal</div>
  <p class="card-copy" style="left:444px">Lorem Ipsum is simply dumm. the printing and typesettin</p>
  <div class="card-link" style="left:444px">FIND OUT MORE &nbsp; &rsaquo;</div>

  <div class="card-photo" style="left:796px;background:linear-gradient(160deg,#3d5a22 0%,#6a7a3a 45%,#8a5a3a 100%)" role="img" aria-label="Tribal elder standing in a jungle"></div>
  <div class="card-label display" style="left:820px">Human</div>
  <p class="card-copy" style="left:798px">Lorem Ipsum is simply dummy text of the printing and typesettin</p>
  <div class="card-link" style="left:798px">FIND OUT MORE &nbsp; &rsaquo;</div>
</section>

<div class="abs divider"></div>

<section class="feature">
  <div class="feature-photo" style="left:82px;top:1540px;background:linear-gradient(170deg,#c27a2c 0%,#6d4428 40%,#3a3028 70%,#5a6a6a 100%)" role="img" aria-label="Mountain coastline with waves at sunset"></div>
  <h2 class="feature-title display" style="left:722px;top:1608px">Environment</h2>
  <p class="feature-copy" style="left:724px;top:1692px">Lorem Ipsum is simply dummy text of the printing and typesetting industry. Lorem Ipsum has been. dustry's standard dummy.</p>
  <div class="btn btn-solid" style="left:723px;top:1797px;width:164px;height:53px">Make a difference</div>
</section>

<section class="feature">
  <div class="abs animal-band"></div>
  <h2 class="feature-title display" style="left:87px;top:2096px;color:var(--white)">Animal</h2>
  <p class="feature-copy" style="left:89px;top:2180px;color:var(--white)">Lorem Ipsum is simply dummy text of the printing and typesetting industry. Lorem Ipsum has been. dustry's standard dummy.</p>
  <div class="btn btn-ghost" style="left:88px;top:2285px;width:164px;height:53px">Make a difference</div>
  <div class="feature-photo" style="left:553px;top:2075px;background:linear-gradient(165deg,#9ab8cc 0%,#6c8a60 40%,#4e9a36 100%)" role="img" aria-label="Zebra in a green field"></div>
</section>

<section class="feature">
  <div class="feature-photo" style="left:82px;top:2545px;background:linear-gradient(160deg,#3c5a22 0%,#6a7a3a 45%,#8c5a3c 100%)" role="img" aria-label="Tribal elder holding a spear in a jungle"></div>
  <h2 class="feature-title display" style="left:722px;top:2613px">Human</h2>
  <p class="feature-copy" style="left:724px;top:2697px">Lorem Ipsum is simply dummy text of the printing and typesetting industry. Lorem Ipsum has been. dustry's standard dummy.</p>
  <div class="btn btn-solid" style="left:723px;top:2802px;width:164px;height:53px">Make a difference</div>
</section>

<footer>
  <div class="abs footer"></div>
  <div class="abs display footer-logo">Open Orbit Charity</div>
  <p class="abs footer-copy">Lorem ipsum is simply dummy text of the printing and typesetting industry. Lorem ipsum.</p>
  <span class="social" style="left:140px"></span>
  <span class="social" style="left:174px"></span>
  <span class="social" style="left:207px"></span>

  <div class="footer-col">
    <h4 style="left:461px">GET INVOLVED</h4>
    <a class="current" style="left:453px;top:3150px">Join Us</a>
    <a style="left:453px;top:3181px">Fundraise</a>
    <a style="left:453px;top:3212px">Donate</a>
    <a style="left:453px;top:3243px">Shop</a>
  </div>
  <div class="footer-col">
    <h4 style="left:692px">GET HELP</h4>
    <a style="left:684px;top:3150px">Contact Us</a>
    <a style="left:684px;top:3181px">Media</a>
  </div>
  <div class="footer-col">
    <h4 style="left:922px">LEGAL</h4>
    <a style="left:914px;top:3150px">Terms and</a>
    <a style="left:914px;top:3181px">Conditions</a>
    <a style="left:914px;top:3212px">Cookies</a>
    <a style="left:914px;top:3243px">Privacy Policy</a>
  </div>
  <div class="abs copyright">Copyright © 2021 Open Orbit Charity. All rights reserved.</div>
</footer>

</body>
</html>
```